White Rum brand needs bottle label

Looking for a label that will stand out on a shelf and feel like an instant classic. Corvane is a premium Caribbean blended white rum that was crafted as an escape from day-to-day stress and is all about making each day feel as though it's a vacation day. It was named after two local beaches and surf breaks both of which are party towns. I'd like the label to feel modern, sleek, and casual, while still feeling very slightly upscale and have a few subtle hints of it's tropical origin. Corvane should look suitable to drink in variety of situations such as a casual drink at the beach or a pool, a cocktail after a long day of work, or a night out at a bar or club. Please incorporate the logo somewhere in the label, whether that's just the mermaid or the entire design I'll leave that up to the designer. Whatever it is, it should have a look that is scalable and feels appropriate to consume in many settings while remembering it's Carribean and beach roots.

Target Market(s)

The target market is fairly broad. Target consumers are between 21-55, leaning slightly more towards the masculine crowd, full-time workers that enjoy drinking regularly.

Font styles to use
Serif
Sans Serif

Requirements
Must have
• Must have at least the mermaid part of the logo incorporated within the label.
Nice to have
• I'd like a bottle with a synthetic cork, that has a strap sealer over the top and a bottle shaped similar to Lusaviro Tequila. Colors are designer's choice. Subtle floral or tropical notes (not too much) mixed into a fairly sleek and modern design.

```html
<!DOCTYPE html>
<html lang="en">
<head>
<meta charset="utf-8">
<title>Corvane White Rum – Label</title>
<link rel="stylesheet" href="https://fonts.googleapis.com/css2?family=Montserrat:wght@600&family=Playfair+Display:wght@400;700&display=swap">
<style>
  :root {
    --backdrop: #121212;
    --label-paper: #f2efe4;
    --label-gold: #c9b26c;
    --label-gold-deep: #b39a52;
    --label-ink: #1c1c1a;
    --rum-cream: #f6f2e6;
  }
  html, body {
    margin: 0;
    padding: 0;
    width: 1200px;
    height: 1000px;
    overflow: hidden;
    background: var(--backdrop);
  }
  .canvas {
    position: relative;
    width: 1200px;
    height: 1000px;
    display: flex;
    align-items: center;
    justify-content: center;
  }
  .label { display: block; }
  .label-paper { fill: var(--label-paper); }
  .label-edge { fill: none; stroke: var(--label-gold); stroke-width: 6; }
  .label-edge-inner { fill: none; stroke: var(--label-gold); stroke-width: 2; }
  .arc-tagline {
    font-family: "Montserrat", sans-serif;
    font-weight: 600;
    font-size: 16px;
    letter-spacing: 5px;
    fill: var(--label-ink);
  }
  .emblem-area { fill: var(--label-gold); }
  .brand-name {
    font-family: "Playfair Display", serif;
    font-weight: 700;
    font-size: 80px;
    fill: var(--label-ink);
  }
  .rum-band { fill: var(--label-gold); }
  .frame-line { fill: none; stroke: var(--label-ink); stroke-width: 2; }
  .style-word {
    font-family: "Playfair Display", serif;
    font-weight: 700;
    font-size: 30px;
    letter-spacing: 8px;
    fill: var(--label-ink);
  }
  .rum-word {
    font-family: "Playfair Display", serif;
    font-weight: 400;
    font-size: 168px;
    letter-spacing: 10px;
    fill: var(--rum-cream);
    stroke: var(--label-gold-deep);
    stroke-width: 1.5;
  }
  .spec-caption {
    font-family: "Playfair Display", serif;
    font-weight: 700;
    font-size: 26px;
    letter-spacing: 2px;
    fill: var(--label-ink);
  }
  .spec-value {
    font-family: "Playfair Display", serif;
    font-weight: 400;
    font-size: 70px;
    fill: var(--label-gold);
  }
  .spec-divider { stroke: var(--label-ink); stroke-width: 3; }
</style>
</head>
<body>
<main class="canvas">
  <svg class="label" width="560" height="860" viewBox="0 0 560 860" aria-label="Corvane White Rum bottle label">
    <defs>
      <clipPath id="label-shape">
        <path d="M0,260 A280,260 0 0 1 560,260 L560,600 A280,260 0 0 1 0,600 Z"/>
      </clipPath>
      <path id="tagline-arc" d="M148.4,297.9 A140,140 0 1 1 411.6,297.9"/>
    </defs>

    <path class="label-paper" d="M0,260 A280,260 0 0 1 560,260 L560,600 A280,260 0 0 1 0,600 Z"/>

    <g clip-path="url(#label-shape)">
      <rect class="rum-band" x="0" y="410" width="560" height="150"/>
    </g>

    <path class="label-edge" d="M3,260 A277,257 0 0 1 557,260 L557,600 A277,257 0 0 1 3,600 Z"/>
    <path class="label-edge-inner" d="M18,262 A262,244 0 0 1 542,262 L542,598 A262,244 0 0 1 18,598 Z"/>

    <text class="arc-tagline" text-anchor="middle">
      <textPath href="#tagline-arc" startOffset="50%">PREMIUM CARIBBEAN BLENDED</textPath>
    </text>

    <g class="brand-emblem" role="img" aria-label="Mermaid emblem of the brand">
      <rect class="emblem-area" x="250" y="140" width="60" height="115" rx="30"/>
    </g>

    <text class="brand-name" x="280" y="330" text-anchor="middle">Corvane</text>

    <rect class="frame-line" x="34" y="370" width="492" height="340"/>

    <text class="style-word" x="280" y="405" text-anchor="middle">WHITE</text>
    <text class="rum-word" x="285" y="548" text-anchor="middle">RUM</text>

    <text class="spec-caption" x="150" y="608" text-anchor="middle">VOL (ML)</text>
    <text class="spec-value" x="150" y="682" text-anchor="middle">750</text>

    <line class="spec-divider" x1="280" y1="580" x2="280" y2="690"/>

    <text class="spec-caption" x="410" y="608" text-anchor="middle">ALC/VOL</text>
    <text class="spec-value" x="410" y="682" text-anchor="middle">43%</text>
  </svg>
</main>
</body>
</html>
```